Vantrel Ashcombe LLC

we need a business card design

Industry/Entity Type

hvac

Contact Information for Business Card

my logo

Requirements
Must have
• my logo and same colors

```html
<!DOCTYPE html>
<html lang="en">
<head>
<meta charset="utf-8">
<title>Vantrel Ashcombe LLC – Business Card</title>
<link href="https://fonts.googleapis.com/css2?family=Arimo:wght@400;700&display=swap" rel="stylesheet">
<style>
  :root {
    --canvas: #e9e6e1;
    --front-light: #0aaee0;
    --front-dark: #0b3a66;
    --back-navy: #020a26;
    --accent-blue: #1ea0dc;
    --accent-gold: #f0a830;
    --text-white: #ffffff;
    --text-dark: #0a1a33;
  }
  * { margin: 0; padding: 0; box-sizing: border-box; }
  html, body {
    width: 1200px; height: 900px; overflow: hidden;
    background: var(--canvas);
    font-family: "Arimo", Arial, sans-serif;
  }
  .stage {
    position: relative; width: 1200px; height: 900px;
  }
  .card {
    position: absolute; left: 275px; width: 650px; height: 372px;
    box-shadow: 0 10px 24px rgba(0,0,0,0.25);
    overflow: hidden;
  }
  .card--front {
    top: 55px;
    border-radius: 36px;
    background: linear-gradient(200deg, var(--front-light) 0%, #1486b8 45%, var(--front-dark) 100%);
  }
  .card--back {
    top: 473px;
    border-radius: 0 60px 0 60px;
    background: var(--back-navy);
  }
  .front-web {
    position: absolute; top: 30px; right: 40px;
    font-size: 15px; font-weight: 700; letter-spacing: 3px;
    color: var(--text-dark);
  }
  .front-web .domain { color: var(--accent-gold); }
  .brand {
    position: absolute; display: flex; align-items: center; gap: 12px;
  }
  .brand-dot {
    width: 22px; height: 22px; border-radius: 50%;
    background: var(--accent-gold); flex-shrink: 0;
  }
  .brand-name {
    font-weight: 700; color: var(--text-white);
    line-height: 1.1; text-transform: uppercase; letter-spacing: 1px;
  }
  .card--front .brand { left: 140px; top: 210px; }
  .card--front .brand-name { font-size: 30px; }
  .card--back .brand { right: 40px; top: 150px; }
  .card--back .brand-name { font-size: 26px; }
  .holder {
    position: absolute; left: 40px; top: 120px; color: var(--text-white);
  }
  .holder-name {
    font-size: 21px; font-weight: 700; color: var(--accent-blue);
    text-transform: uppercase;
  }
  .holder-role {
    font-size: 16px; margin-top: 4px; padding-bottom: 6px;
    border-bottom: 1px solid var(--accent-gold); width: 90px;
  }
  .address { margin-top: 26px; font-size: 16px; line-height: 1.3; }
  .contacts { list-style: none; margin-top: 14px; font-size: 16px; }
  .contacts li { display: flex; align-items: center; gap: 10px; margin-top: 6px; }
  .contacts svg { width: 16px; height: 16px; flex-shrink: 0; }
  .contacts .hl { color: var(--accent-blue); }
</style>
</head>
<body>
<main class="stage">
  <section class="card card--front" aria-label="Card front">
    <p class="front-web">www.<span class="domain">vantrelashcombe</span>.com</p>
    <div class="brand">
      <span class="brand-dot"></span>
      <span class="brand-name">Vantrel Ashcombe<br>LLC</span>
    </div>
  </section>

  <section class="card card--back" aria-label="Card back">
    <div class="holder">
      <h1 class="holder-name">Dorian Kell</h1>
      <p class="holder-role">Director</p>
      <p class="address">00 dummy city<br>dummy place 0000</p>
      <ul class="contacts">
        <li>
          <svg viewBox="0 0 16 16"><path fill="#1ea0dc" d="M3 1l3 3-2 2c1 2 3 4 5 5l2-2 3 3-2 3C7 15 1 9 0 4z"/></svg>
          <span>555-204-9130</span>
        </li>
        <li>
          <svg viewBox="0 0 16 16"><rect x="1" y="3" width="14" height="10" fill="none" stroke="#1ea0dc" stroke-width="1.5"/><path d="M1 3l7 6 7-6" fill="none" stroke="#1ea0dc" stroke-width="1.5"/></svg>
          <span>info@<span class="hl">vantrelashcombe</span>.com</span>
        </li>
        <li>
          <svg viewBox="0 0 16 16"><circle cx="8" cy="8" r="7" fill="none" stroke="#1ea0dc" stroke-width="1.3"/><ellipse cx="8" cy="8" rx="3" ry="7" fill="none" stroke="#1ea0dc" stroke-width="1.1"/><path d="M1 8h14" stroke="#1ea0dc" stroke-width="1.1"/></svg>
          <span>www.<span class="hl">vantrelashcombe</span>.com</span>
        </li>
      </ul>
    </div>
    <div class="brand">
      <span class="brand-dot"></span>
      <span class="brand-name">Vantrel Ashcombe<br>LLC</span>
    </div>
  </section>
</main>
</body>
</html>
```